Video Editing Website - Wordpress Design Project

Hi There
I am setting up a Tribute Funeral Video and Home Video Editing Website for my Company. "Cut My Reel". This is to assist people with putting together their Videos and Photos with music to show at a Funeral or for Family Memories. I already have a domain www.cutmyreel.com.au, but I have no host yet.

Some websites that already do this are http://www.farewellclips.com.au/tributes, http://www.familyfilmcrafting.com.au/services/funeral-tribute-videos.html, and http://www.memorialslideworks.com.au/
These are examples not to cpy, but to get an idea of what I am offering so you can design accordingly.

I have a logo which is attached. You will see that the logo is mainly blue, so I would appreciate a website with that colour on the pages, but not ALL over the page.

I would like to upload videos occasionally from clipnest.com so I would appreciate that option incorporated.

Thank you lots.
Gareth

Target Market(s)

Families predominately in the 25-60 age range

Industry/Entity Type

It Company

Requirements
Must have
• *Ability to upload Videos from clipnest.com
*Ability for me to edit the content whenever I need to
*A contact page to send email messages to me

```html
<!DOCTYPE html>
<html lang="en">
<head>
<meta charset="utf-8">
<title>Cut My Reel – Tribute Funeral Video</title>
<link href="https://fonts.googleapis.com/css2?family=Arvo:wght@400;700&family=PT+Sans:wght@400;700&display=swap" rel="stylesheet">
<style>
:root{
  --blue:#0b5cba;
  --blue-dark:#084a99;
  --ink:#222;
  --muted:#8a8a8a;
  --panel:#f0f0f0;
  --line:#dcdcdc;
  --white:#fff;
}
*{box-sizing:border-box;margin:0;padding:0}
html,body{width:1079px;height:1200px;overflow:hidden;background:var(--white)}
body{font-family:"PT Sans",sans-serif;color:var(--ink);position:relative}
.page{position:relative;width:1079px;height:1200px}
.abs{position:absolute}

/* header */
.brand{left:113px;top:30px;display:flex;align-items:flex-end;gap:8px;height:106px}
.brand-mark{width:22px;height:22px;border-radius:50%;background:var(--blue);margin-bottom:10px}
.brand-name{font-size:30px;color:var(--blue);font-weight:400;line-height:1;margin-bottom:6px}
.contact{right:104px;top:94px;text-align:right;font-size:15px;line-height:25px;color:#222}

/* nav */
.nav{left:113px;top:146px;width:862px;height:51px;background:var(--blue);display:flex;align-items:center;padding-left:31px}
.nav a{color:var(--white);text-decoration:none;font-size:14px}
.nav .sep{color:var(--white);margin:0 13px;font-size:14px}
.search{position:absolute;right:13px;top:13px;width:224px;height:25px;background:#f4f4f4;border:1px solid #c9d6e6;display:flex;align-items:center;justify-content:space-between;padding:0 6px 0 8px;font-size:8px;color:#aaa}

/* hero */
.hero{left:113px;top:205px;width:862px;height:325px;background:linear-gradient(100deg,#4c7a2a 0%,#6f9b3c 35%,#8c9d86 60%,#a9a7b8 80%,#d9d3d8 100%)}
.hero-title{left:40px;top:128px;color:var(--white);font-family:"Arvo",serif;text-shadow:0 1px 3px rgba(0,0,0,.4)}
.hero-title .big{font-size:38px;line-height:40px;display:block}
.hero-title .small{font-size:23px;line-height:30px;display:block}
.dots{right:16px;bottom:15px;display:flex;gap:3px}
.dots span{width:12px;height:12px;border-radius:50%;background:#222;border:1px solid #fff}
.dots span.on{background:#fff;border-color:#222}

/* welcome */
.welcome-title{left:0;top:556px;width:1079px;text-align:center;font-family:"Arvo",serif;font-size:16px;color:#333}
.welcome-text{left:113px;top:588px;width:862px;text-align:center;font-size:11.5px;line-height:20px;color:var(--muted)}

/* columns */
.col-title{top:696px;font-family:"Arvo",serif;font-size:16px;color:#333}
.arrows{left:935px;top:694px;display:flex;gap:10px}
.box{top:728px;width:281px;height:283px}
.feature{left:113px;background:var(--blue)}
.feature-media{height:220px;background:linear-gradient(180deg,#e6e0d6 0%,#c9a8a0 45%,#8a5a3a 100%);position:relative}
.play{position:absolute;left:113px;top:97px;width:58px;height:34px;background:rgba(0,0,0,.55)}
.player{position:absolute;left:0;bottom:0;width:100%;height:22px;background:rgba(20,20,20,.85)}
.player .track{position:absolute;left:13px;top:9px;width:210px;height:4px;background:#666}
.player .fill{position:absolute;left:0;top:0;width:90px;height:4px;background:#3a8fe0}
.feature-caption{padding:7px 13px;color:var(--white);font-size:11.5px;line-height:18px}

.videos{left:404px;background:var(--panel);padding:14px 11px 0}
.vrow{display:flex;gap:11px;height:69px}
.thumb{width:80px;height:58px;flex:none;position:relative}
.thumb::after{content:"";position:absolute;left:32px;top:23px;border-left:8px solid #fff;border-top:5px solid transparent;border-bottom:5px solid transparent}
.t1{background:radial-gradient(circle,#e8c020 0%,#8a9a40 60%,#dcdcdc 100%)}
.t2{background:linear-gradient(135deg,#a01010,#d02020,#601010)}
.t3{background:linear-gradient(180deg,#d8c8d0,#7a3a4a 70%,#3a2020)}
.vtext h4{font-size:11.5px;font-weight:400;color:#111;line-height:16px}
.vtext p{font-size:11px;line-height:16px;color:var(--muted);width:160px}
.rule{border-top:1px solid var(--line);margin-top:7px}
.btn{display:block;margin:20px auto 0;background:var(--blue);color:var(--white);font-size:12px;border-radius:2px;width:99px;height:23px;line-height:23px;text-align:center}

.photos{left:694px;background:var(--panel);padding:19px 17px 0}
.photo{height:188px;background:linear-gradient(180deg,#e6ebe6 0%,#dfe6e0 55%,#9ab080 80%,#f0f0e8 100%)}
.photos .rule{margin-top:15px}
.photos .btn{margin-top:20px}

/* newsletter */
.news{left:110px;top:1043px;width:863px;height:73px;background:var(--blue);border-radius:3px;display:flex;align-items:center;padding:0 16px 0 23px}
.news-label{color:var(--white);font-size:14px;margin-left:10px;width:118px}
.news-input{width:551px;height:33px;background:var(--white);border:1px solid #c8c8c8;font-size:12px;color:#b8b8b8;line-height:31px;padding-left:11px}
.news-submit{margin-left:10px;width:105px;height:36px;border-radius:3px;background:linear-gradient(#fff,#e8e8e8);font-size:16px;color:#333;text-align:center;line-height:36px}

/* footer */
.foot-nav{left:113px;top:1145px;font-size:13px;color:#222}
.foot-nav .sep{margin:0 11px}
.copy{left:113px;top:1174px;font-size:13px;color:#444}
.social{left:850px;top:1155px;display:flex;gap:2px}
.social span{width:30px;height:30px;border-radius:50%;background:#111}
</style>
</head>
<body>
<div class="page">

  <div class="abs brand">
    <span class="brand-mark"></span>
    <span class="brand-name">cutmyreel</span>
  </div>
  <div class="abs contact">
    E-mail : hello@reelmail.com.au<br>
    Tel : (03) 5550 1942 Fax: (03) 5550 1943
  </div>

  <nav class="abs nav">
    <a href="#">Home</a><span class="sep">|</span>
    <a href="#">About Us</a><span class="sep">|</span>
    <a href="#">Videos</a><span class="sep">|</span>
    <a href="#">Photos</a><span class="sep">|</span>
    <a href="#">Music</a><span class="sep">|</span>
    <a href="#">Testimonials</a><span class="sep">|</span>
    <a href="#">Contact Us</a>
    <div class="search">Type search
      <svg width="11" height="11" viewBox="0 0 11 11"><circle cx="4.5" cy="4.5" r="3.3" fill="none" stroke="#999" stroke-width="1.2"/><line x1="7" y1="7" x2="10" y2="10" stroke="#999" stroke-width="1.4"/></svg>
    </div>
  </nav>

  <div class="abs hero" role="img" aria-label="Photo of a casket with a white and yellow flower spray at a graveside, draped chairs on green lawn">
    <div class="abs hero-title"><span class="big">TRIBUTE</span><span class="small">Funeral Video</span></div>
    <div class="abs dots"><span class="on"></span><span></span><span></span><span></span></div>
  </div>

  <h2 class="abs welcome-title">Welcome To Cut My Reel</h2>
  <p class="abs welcome-text">Lorem Ipsum is simply dummy text of the printing and typesetting industry. Lorem Ipsum has been the industry's standard dummy text ever since the 1500s, when an unknown printer took a galley of type and scrambled it to make a type specimen book. It has survived not only five centuries, but also the leap into electronic typesetting, remaining essentially unchanged. It was popularised in the 1960s with the release of Letraset sheets containing Lorem Ipsum passages, and more recently with desktop publishing software like Aldus PageMaker including versions of Lorem Ipsum.</p>

  <h3 class="abs col-title" style="left:117px">Tribute Funeral Video</h3>
  <h3 class="abs col-title" style="left:404px">Videos</h3>
  <h3 class="abs col-title" style="left:693px">Photos</h3>
  <div class="abs arrows">
    <svg width="14" height="20" viewBox="0 0 14 20"><polyline points="11,2 3,10 11,18" fill="none" stroke="#444" stroke-width="2.5"/></svg>
    <svg width="14" height="20" viewBox="0 0 14 20"><polyline points="3,2 11,10 3,18" fill="none" stroke="#444" stroke-width="2.5"/></svg>
  </div>

  <div class="abs box feature">
    <div class="feature-media" role="img" aria-label="Video still of a large colourful funeral flower arrangement on a wooden casket">
      <div class="play"><svg width="58" height="34" viewBox="0 0 58 34"><polygon points="25,11 25,23 35,17" fill="#fff"/></svg></div>
      <div class="player"><div class="track"><div class="fill"></div></div></div>
    </div>
    <p class="feature-caption">Lorem Ipsum is simply dummy text of the printing and typesetting industry. Lorem Ipsum has been the industry's standard dummy text book.</p>
  </div>

  <div class="abs box videos">
    <div class="vrow">
      <div class="thumb t1" role="img" aria-label="Yellow flower wreath video thumbnail"></div>
      <div class="vtext"><h4>In memories of daniel hartley</h4><p>Lorem Ipsum is simply dummy text of the printing and typeset-ting industry.</p></div>
    </div>
    <div class="vrow" style="margin-top:6px">
      <div class="thumb t2" role="img" aria-label="Red roses video thumbnail"></div>
      <div class="vtext"><h4>In memories of daniel hartley</h4><p>Lorem Ipsum is simply dummy text of the printing and typeset-ting industry.</p></div>
    </div>
    <div class="vrow" style="margin-top:6px">
      <div class="thumb t3" role="img" aria-label="Casket with flowers video thumbnail"></div>
      <div class="vtext"><h4>In memories of daniel hartley</h4><p>Lorem Ipsum is simply dummy text of the printing and typeset-ting industry.</p></div>
    </div>
    <div class="rule"></div>
    <span class="btn">Submit Video</span>
  </div>

  <div class="abs box photos">
    <div class="photo" role="img" aria-label="Memorial photo card with white roses and a forever in our hearts ribbon"></div>
    <div class="rule"></div>
    <span class="btn">Submit Photo</span>
  </div>

  <div class="abs news">
    <svg width="38" height="26" viewBox="0 0 38 26"><rect x="1" y="1" width="36" height="24" fill="none" stroke="#fff" stroke-width="1.6"/><polyline points="1,1 19,15 37,1" fill="none" stroke="#fff" stroke-width="1.6"/><line x1="1" y1="25" x2="14" y2="11" stroke="#fff" stroke-width="1.4"/><line x1="37" y1="25" x2="24" y2="11" stroke="#fff" stroke-width="1.4"/></svg>
    <span class="news-label">Sign up newsletter</span>
    <div class="news-input">Enter the E-mail Address</div>
    <div class="news-submit">Submit</div>
  </div>

  <div class="abs foot-nav">Home<span class="sep">|</span>About Us<span class="sep">|</span>Videos<span class="sep">|</span>Photos<span class="sep">|</span>Music<span class="sep">|</span>Testimonials<span class="sep">|</span>Contact Us</div>
  <div class="abs copy">©2013 Company Name , All Rights Reserved</div>
  <div class="abs social" aria-label="Social links">
    <span></span><span></span><span></span><span></span>
  </div>

</div>
</body>
</html>
```